[AMAZING DESIGN NEEDED] Women's Fishing Squeeze Page

I need a professional design for a landing page that is going to collect email addresses.

You can use the creatives already on the page or you can pull images from the facebook/instagram pages.
https://www.facebook.com/LakesLuresBoots
https://www.instagram.com/lakesluresandboots/

This is the page that needs designed: https://lakesluresandboots.example/email-opt-in/

See attached for examples.

Target Market(s)

Women who like to go fishing

Industry/Entity Type

Fishing

Number of Pages Required

1 page

Font styles to use
Sans Serif

Requirements
Must have
• excellent design. Call to actions.

```html
<!DOCTYPE html>
<html lang="en">
<head>
<meta charset="utf-8">
<title>Lakes, Lures &amp; Boots — Sign Up</title>
<link href="https://fonts.googleapis.com/css2?family=Oswald:wght@400;500;600&family=DM+Sans:wght@400;500;700&display=swap" rel="stylesheet">
<style>
:root{
  --brown:#9a7549;
  --teal:#3aa8ac;
  --tan:#c8ad92;
  --ink:#3a3a3a;
  --ink-soft:#4a3f35;
  --white:#ffffff;
  --line:#d9d9d9;
}
*{box-sizing:border-box;margin:0;padding:0}
html,body{width:1022px;height:1200px;overflow:hidden}
body{position:relative;font-family:"DM Sans",sans-serif;color:var(--ink);background:var(--tan)}
.abs{position:absolute}
.topbar{left:0;top:0;width:1022px;height:41px;background:var(--brown);color:var(--white);font-size:11px}
.social{display:flex;gap:11px;left:132px;top:12px}
.social span{width:16px;height:16px;border-radius:3px;background:var(--white);display:block}
.search{left:425px;top:11px;width:109px;padding-bottom:6px;border-bottom:1px solid rgba(255,255,255,.35);display:flex;align-items:center;gap:10px}
.toplinks{left:554px;top:14px;display:flex;gap:24px;align-items:center}
.toplinks b{font-weight:700}
.hero{left:0;top:41px;width:1022px;height:567px}
.photo{position:absolute;inset:0;background:linear-gradient(180deg,#dfe9f3 0%,#b9c9d6 18%,#7f8f78 34%,#3d5a3a 55%,#5c7b86 68%,#8fa8b0 85%,#6f8990 100%)}
.brand{left:133px;top:66px;font-family:"DM Sans",sans-serif;font-weight:700;font-size:16px;color:var(--teal);display:flex;align-items:center;gap:6px}
.brand i{width:12px;height:12px;border-radius:50%;background:var(--teal);display:block}
.nav{left:265px;top:87px;display:flex;gap:16px;font-size:11px;font-weight:500;color:var(--ink)}
.phone-btn{left:755px;top:72px;width:133px;height:40px;background:var(--teal);color:var(--white);font-family:"Oswald",sans-serif;font-weight:500;font-size:17px;display:flex;align-items:center;justify-content:center;gap:8px}
.signup{left:586px;top:166px;width:302px;height:378px;border:7px solid var(--brown);background:var(--white)}
.signup-head{height:107px;background:#f6f3ee;position:relative;border-bottom:2px dotted #c9b79f}
.mascot{position:absolute;left:17px;top:13px;width:44px;height:46px;background:linear-gradient(#e8c9a0,#6aa38a);border-radius:4px}
.signup h2{position:absolute;left:74px;top:20px;font-family:"Oswald",sans-serif;font-weight:600;font-size:33px;color:var(--ink);letter-spacing:.5px}
.signup h2 em{font-style:normal;color:var(--brown)}
.signup p{position:absolute;left:18px;top:69px;font-family:"Oswald",sans-serif;font-size:15px;letter-spacing:1px;color:var(--ink)}
.signup p em{font-style:normal;color:var(--teal);font-weight:500}
.field{position:absolute;left:19px;width:253px;height:46px;border:1px solid var(--line);display:flex;align-items:center;gap:11px;padding-left:15px;font-size:13px;color:#9a9a9a}
.field svg{flex:none}
.cta{position:absolute;left:19px;top:303px;width:253px;height:47px;background:var(--teal);color:var(--white);font-family:"Oswald",sans-serif;font-weight:500;font-size:19px;display:flex;align-items:center;justify-content:center}
.newsletter{left:0;top:608px;width:1022px;height:183px;background:var(--teal)}
.newsletter h3{position:absolute;left:133px;top:65px;font-family:"Oswald",sans-serif;font-weight:500;font-size:22px;color:var(--white)}
.newsletter p{position:absolute;left:133px;top:106px;font-size:12px;color:#21484a}
.nl-input{position:absolute;left:521px;top:68px;width:233px;height:52px;background:var(--white);padding-left:24px;display:flex;align-items:center;font-size:13px;color:#a6a6a6}
.nl-btn{position:absolute;left:754px;top:68px;width:135px;height:52px;background:var(--brown);color:var(--white);font-family:"Oswald",sans-serif;font-weight:500;font-size:14px;display:flex;align-items:center;justify-content:center;gap:14px}
.col{top:846px;width:180px}
.col h4{font-family:"Oswald",sans-serif;font-weight:500;font-size:17px;color:var(--ink-soft);padding-bottom:8px;position:relative}
.col h4::after{content:"";position:absolute;left:0;bottom:0;width:18px;height:1px;background:var(--brown)}
.col ul{list-style:none;margin-top:12px;font-size:11px;color:var(--ink-soft)}
.col li{height:24.5px}
.col .ph{display:flex;align-items:center;gap:8px;font-family:"Oswald",sans-serif;font-weight:500;font-size:17px;margin-top:-2px}
.col .soc{display:flex;gap:11px;margin-top:14px}
.col .soc span{width:16px;height:16px;border-radius:3px;background:var(--ink-soft);display:block}
.pay{left:0;top:1065px;width:1022px;height:54px;border-top:1px solid #b99e82;border-bottom:1px solid #b99e82}
.pay .cell{position:absolute;top:0;height:53px;border-left:1px solid #b99e82;display:flex;align-items:center;justify-content:center;font-weight:700;font-size:14px;color:#6d5b49}
.copy{left:0;top:1153px;width:1022px;text-align:center;font-size:10px;color:var(--ink-soft)}
</style>
</head>
<body>
<header class="abs topbar">
  <div class="abs social"><span aria-label="Social profile"></span><span aria-label="Photo profile"></span></div>
  <div class="abs search">
    <svg width="13" height="13" viewBox="0 0 16 16"><circle cx="6.5" cy="6.5" r="5" fill="none" stroke="#fff" stroke-width="2.2"/><path d="M10.5 10.5 15 15" stroke="#fff" stroke-width="2.4"/></svg>Search
  </div>
  <div class="abs toplinks">
    <span>Get Certificates</span>
    <span><b>SIGN IN</b> or <b>REGISTER</b></span>
    <span>Cart [0]</span>
  </div>
</header>

<section class="abs hero">
  <div class="photo" role="img" aria-label="Woman fly fishing in a mountain lake under a blue sky"></div>
  <div class="abs brand" style="top:25px"><i></i>Lakes, Lures &amp; Boots</div>
  <nav class="abs nav" style="top:46px"><span>CLOTHING</span><span>HATS</span><span>BUNDLES</span><span>ACCESSORIES &amp; STICKERS</span><span>JEWELRY</span><span>CLEARANCE</span></nav>
  <div class="abs phone-btn" style="top:31px">
    <svg width="15" height="15" viewBox="0 0 24 24"><path fill="#fff" d="M6.6 10.8a15 15 0 0 0 6.6 6.6l2.2-2.2a1 1 0 0 1 1-.25 11.4 11.4 0 0 0 3.6.57 1 1 0 0 1 1 1V20a1 1 0 0 1-1 1A17 17 0 0 1 3 4a1 1 0 0 1 1-1h3.5a1 1 0 0 1 1 1c0 1.25.2 2.45.57 3.57a1 1 0 0 1-.25 1z"/></svg>4065550142
  </div>
  <form class="abs signup" style="top:125px">
    <div class="signup-head">
      <div class="mascot" role="img" aria-label="Cartoon angler holding a rod"></div>
      <h2>SIGN UP <em>TODAY</em></h2>
      <p>AND RECEIVE <em>15% OFF</em> YOUR NEXT ORDER</p>
    </div>
    <div class="field" style="top:132px"><svg width="15" height="15" viewBox="0 0 16 16"><circle cx="8" cy="5" r="3.3" fill="none" stroke="#b48a5a" stroke-width="1.3"/><path d="M2 15c0-3.5 2.7-5.5 6-5.5s6 2 6 5.5z" fill="none" stroke="#b48a5a" stroke-width="1.3"/></svg>First name</div>
    <div class="field" style="top:186px"><svg width="15" height="15" viewBox="0 0 16 16"><circle cx="8" cy="5" r="3.3" fill="none" stroke="#b48a5a" stroke-width="1.3"/><path d="M2 15c0-3.5 2.7-5.5 6-5.5s6 2 6 5.5z" fill="none" stroke="#b48a5a" stroke-width="1.3"/></svg>Last name</div>
    <div class="field" style="top:241px"><svg width="16" height="13" viewBox="0 0 16 12"><rect x=".7" y=".7" width="14.6" height="10.6" fill="none" stroke="#b48a5a" stroke-width="1.3"/><path d="M1 1l7 6 7-6" fill="none" stroke="#b48a5a" stroke-width="1.3"/></svg>Email address *</div>
    <div class="cta">SUBSCRIBE &amp; SAVE</div>
  </form>
</section>

<section class="abs newsletter">
  <h3>Subscribe to Our Newsletter</h3>
  <p>Get the latest updates on new products and upcoming sales</p>
  <div class="nl-input">Your Email address</div>
  <div class="nl-btn">SUBSCRIBE
    <svg width="22" height="20" viewBox="0 0 24 22"><path d="M23 1 3 10l7 2 2 8 3-6z" fill="none" stroke="#fff" stroke-width="1.6" stroke-linejoin="round"/><path d="M23 1 10 12" stroke="#fff" stroke-width="1.4"/></svg>
  </div>
</section>

<div class="abs col" style="left:133px"><h4>Navigate</h4><ul><li>Trips</li><li>Shipping &amp; Returns</li><li>Contact Us</li><li>Blog</li><li>Sitemap</li></ul></div>
<div class="abs col" style="left:327px"><h4>Categories</h4><ul><li>Clothing</li><li>Hats</li><li>Bundles</li><li>Accessories &amp; Stickers</li><li>Jewelry</li><li>Clearance</li></ul></div>
<div class="abs col" style="left:521px"><h4>Info</h4><ul><li>Montana</li><li class="ph"><svg width="14" height="14" viewBox="0 0 24 24"><path fill="#4a3f35" d="M6.6 10.8a15 15 0 0 0 6.6 6.6l2.2-2.2a1 1 0 0 1 1-.25 11.4 11.4 0 0 0 3.6.57 1 1 0 0 1 1 1V20a1 1 0 0 1-1 1A17 17 0 0 1 3 4a1 1 0 0 1 1-1h3.5a1 1 0 0 1 1 1c0 1.25.2 2.45.57 3.57a1 1 0 0 1-.25 1z"/></svg>4065550142</li></ul></div>
<div class="abs col" style="left:716px"><h4>Connect With Us</h4><div class="soc"><span aria-label="Social profile"></span><span aria-label="Photo profile"></span></div></div>

<div class="abs pay">
  <div class="cell" style="left:133px;width:149px">Amberline</div>
  <div class="cell" style="left:282px;width:158px">Northpay</div>
  <div class="cell" style="left:440px;width:157px">Rivercard</div>
  <div class="cell" style="left:597px;width:140px">Lakepay</div>
  <div class="cell" style="left:737px;width:150px;border-right:1px solid #b99e82">Trailcard</div>
</div>

<p class="abs copy">Copyright © 2021 Lakes, Lures &amp; Boots. All rights reserved</p>
</body>
</html>
```